Velmora Skincare packaging designs

We are need to create packaging for our skincare brand. We need two designs. One for round jars which is for creams/capsules and the second will be for bottles/serums Some products will be larger in size so please ensure the packaging design will work and there isn't a lot white/empty space

Below are the names of some of our products.
Screw-On Top Jar (25 pads- 4 inches wide) - Glint Wipes I Skin Brightening Pads
Pump Bottle (2 oz) - Rekindle I Hyaluronic Acid + Vitamin Serum
Pump Bottle (6oz) - The Cloud Rinse I Conditioning Face Cleanser
Dropper bottle (1 oz) - Sunny Veil I Hydrating Moisturizer
Cream jar (1.5 oz) - Sunny Veil I Hydrating Moisturizer
Capsules Jar (25 capsules in a jar)- Lumo Burst I Moisture + Hydrating Capsules
Capsules Jar (25 capsules in a jar) - Pure Spark I Impurity Capsules

We will also need help with the packing design in terms of layout of the logo, item name, desc, and ingredients on each product.

Target Market(s)

women

Industry/Entity Type

skincare, beauty

Font styles to use
Sans Serif

Colors
E54698
E96AAD
F1A4CE
F9D9EA
FCEFF6

Requirements
Must have
• Pantone color is 2052 CP HEX #DAAFCA (218 , 175 , 202)

```html
<!DOCTYPE html>
<html lang="en">
<head>
<meta charset="utf-8">
<title>Velmora Skincare – Packaging Range</title>
<link rel="stylesheet" href="https://fonts.googleapis.com/css2?family=Oswald:wght@300;400&display=swap">
<style>
  :root{
    --backdrop:#D6789F;
    --white:#FFFFFF;
    --off-white:#F6F1F4;
    --cap-shade:#ECE6EA;
    --band:#E393B6;
    --brand-ink:#E08AAF;
    --glass:#C9C6CA;
    --glass-light:#EDEBEE;
  }
  *{margin:0;padding:0;box-sizing:border-box}
  html,body{width:1200px;height:646px;overflow:hidden}
  body{background:var(--backdrop);font-family:"Oswald",sans-serif;font-weight:300;color:var(--white)}
  .range{position:relative;width:1200px;height:646px}
  .part{position:absolute}
  .logo{position:absolute;color:var(--brand-ink);font-weight:300;letter-spacing:.14em;text-align:center;white-space:nowrap;line-height:1}
  .logo-vertical{writing-mode:vertical-rl;transform:rotate(180deg)}
  .size-badge{position:absolute;border-radius:50%;background:var(--band);color:var(--white);display:flex;flex-direction:column;align-items:center;justify-content:center;line-height:1}
  .size-badge .num{font-weight:400}
  .size-badge .unit{font-size:5px;letter-spacing:.05em;margin-top:1px}
  .band{position:absolute;background:var(--band);display:flex;align-items:center;justify-content:center;gap:6px;text-transform:uppercase;line-height:1.15;white-space:nowrap}
  .band .divider{width:1px;align-self:stretch;margin:6px 0;background:var(--white)}
  .band .col{display:flex;flex-direction:column;white-space:nowrap}

  /* dropper bottle */
  .dropper-bulb{left:185px;top:348px;width:33px;height:54px;background:var(--off-white);border-radius:16px 16px 3px 3px}
  .dropper-collar{left:172px;top:400px;width:58px;height:45px;background:repeating-linear-gradient(90deg,var(--white) 0 4px,var(--cap-shade) 4px 6px);border-radius:3px}
  .dropper-neck{left:170px;top:445px;width:62px;height:36px;background:linear-gradient(90deg,var(--glass),var(--glass-light),var(--glass))}
  .dropper-body{left:160px;top:478px;width:85px;height:137px;background:linear-gradient(90deg,var(--glass) 0,var(--glass-light) 25%,var(--white) 50%,var(--glass-light) 75%,var(--glass) 100%);border-radius:14px}
  .dropper-band{left:160px;top:570px;width:85px;height:33px;font-size:8px;gap:5px}

  /* cleanser tube */
  .tube-crimp{left:290px;top:227px;width:148px;height:8px;background:var(--white);border-radius:2px}
  .tube-body{left:290px;top:234px;width:148px;height:374px;background:var(--white);clip-path:polygon(0 0,100% 0,84% 100%,18% 100%);border-radius:0 0 10px 10px}
  .tube-band{left:310px;top:505px;width:110px;height:48px;font-size:9px;gap:5px}

  /* large pump bottle */
  .pump-head{background:var(--white);border-radius:2px}
  .bottle-body{left:486px;top:210px;width:136px;height:390px;background:var(--white);border-radius:62px 62px 16px 16px}
  .bottle-band{left:486px;top:548px;width:136px;height:50px;font-size:12px}

  /* small pump bottle */
  .small-body{left:695px;top:403px;width:133px;height:187px;background:var(--white);border-radius:52px 52px 14px 14px}
  .small-band{left:695px;top:546px;width:133px;height:42px;font-size:9px;gap:7px}

  /* pad jar */
  .jar-lid{left:924px;top:395px;width:160px;height:32px;background:linear-gradient(var(--white),var(--cap-shade));border-radius:10px 10px 3px 3px}
  .jar-body{left:926px;top:427px;width:156px;height:95px;background:var(--white);border-radius:2px 2px 8px 8px}
  .jar-band{left:926px;top:488px;width:156px;height:26px;font-size:9.5px;letter-spacing:.02em}

  /* mini tube */
  .mini-nozzle{left:856px;top:566px;width:30px;height:10px;background:var(--white);border-radius:4px 0 0 4px}
  .mini-body{left:885px;top:548px;width:180px;height:42px;background:var(--white);border-radius:6px 0 0 6px}
  .mini-crimp{left:1062px;top:545px;width:24px;height:48px;background:var(--band);color:var(--white);font-size:5px;line-height:1.1;writing-mode:vertical-rl;transform:rotate(180deg);display:flex;align-items:center;justify-content:center;text-transform:uppercase;white-space:nowrap}
</style>
</head>
<body>
<main class="range">

  <section class="product product-dropper">
    <div class="part dropper-bulb"></div>
    <div class="part dropper-collar"></div>
    <div class="part dropper-neck"></div>
    <div class="part dropper-body"></div>
    <div class="size-badge" style="left:190px;top:497px;width:24px;height:24px"><span class="num" style="font-size:11px">1</span><span class="unit">FL OZ</span></div>
    <div class="logo" style="left:160px;top:531px;width:85px;font-size:12px">VELMORA</div>
    <div class="band dropper-band">
      <div class="col"><span>Sunny</span><span>Veil</span></div>
      <span class="divider"></span>
      <div class="col"><span>Hydrating</span><span>Moisturizer</span></div>
    </div>
  </section>

  <section class="product product-tube">
    <div class="part tube-crimp"></div>
    <div class="part tube-body"></div>
    <div class="logo logo-vertical" style="left:347px;top:262px;font-size:40px;letter-spacing:.1em">VELMORA</div>
    <div class="band tube-band">
      <div class="col"><span>Conditioning</span><span>Face Cleanser</span></div>
      <span class="divider"></span>
      <div class="col"><span>The Cloud</span><span>Rinse</span></div>
    </div>
  </section>

  <section class="product product-bottle">
    <div class="part pump-head" style="left:538px;top:112px;width:74px;height:6px"></div>
    <div class="part pump-head" style="left:545px;top:117px;width:20px;height:55px;background:var(--cap-shade)"></div>
    <div class="part pump-head" style="left:526px;top:170px;width:56px;height:42px;background:repeating-linear-gradient(90deg,var(--white) 0 3px,var(--off-white) 3px 5px)"></div>
    <div class="part bottle-body"></div>
    <div class="size-badge" style="left:536px;top:242px;width:35px;height:35px"><span class="num" style="font-size:15px">6</span><span class="unit" style="font-size:6px">FL OZ</span></div>
    <div class="logo logo-vertical" style="left:530px;top:292px;font-size:46px;letter-spacing:.1em">VELMORA</div>
    <div class="band bottle-band">
      <div class="col"><span>Conditioning</span><span>Face Cleanser</span></div>
      <span class="divider"></span>
      <div class="col"><span>The Cloud</span><span>Rinse</span></div>
    </div>
  </section>

  <section class="product product-serum">
    <div class="part pump-head" style="left:738px;top:307px;width:82px;height:6px"></div>
    <div class="part pump-head" style="left:755px;top:312px;width:16px;height:50px;background:var(--cap-shade)"></div>
    <div class="part pump-head" style="left:734px;top:360px;width:54px;height:44px;background:repeating-linear-gradient(90deg,var(--white) 0 3px,var(--off-white) 3px 5px)"></div>
    <div class="part small-body"></div>
    <div class="size-badge" style="left:745px;top:441px;width:30px;height:30px"><span class="num" style="font-size:13px">2</span><span class="unit">FL OZ</span></div>
    <div class="logo" style="left:695px;top:490px;width:133px;font-size:19px;letter-spacing:.12em">VELMORA</div>
    <div class="band small-band">
      <span style="font-size:10px">Rekindle</span>
      <span class="divider"></span>
      <div class="col"><span>Hyaluronic Acid</span><span>+ Vitamin Serum</span></div>
    </div>
  </section>

  <section class="product product-jar">
    <div class="part jar-lid"></div>
    <div class="part jar-body"></div>
    <div class="logo" style="left:926px;top:442px;width:156px;font-size:21px;letter-spacing:.12em">VELMORA</div>
    <div class="band jar-band"><span>Glint Wipes I Skin Brightening Pads</span></div>
  </section>

  <section class="product product-mini">
    <div class="part mini-nozzle"></div>
    <div class="part mini-body"></div>
    <div class="size-badge" style="left:906px;top:558px;width:21px;height:21px"><span class="num" style="font-size:8px">0.3</span><span class="unit" style="font-size:4px">FL OZ</span></div>
    <div class="logo" style="left:935px;top:560px;width:120px;font-size:18px;letter-spacing:.1em">VELMORA</div>
    <div class="part mini-crimp"><span>Conditioning<br>Face Cleanser</span></div>
  </section>

</main>
</body>
</html>
```